Introduction to a startup providing solutions for energy sector

Email campaign to introduce a startup classified portal for the oil and gas industry that lists surplus material for sale, the startup is intending to tackle this major issue in the industry of having excess material laying around year on year in warehouses, Vorlinex will gather the data and conduct and inspection for the material before listing it, so buyers can inquire and purchase with confidence

Target Market(s)

Energy Sector

Font styles to use
Serif

Colors

Designer to choose only greyscale colors for use in the design.

Requirements
Must have
• friendly look not congested, present some elements from the attached presentation, whatever helps intrigues buyers to visit the website, the colors grey, blue and white colors (like the logo)
Should not have
• to many colors

```html
<!DOCTYPE html>
<html lang="en">
<head>
<meta charset="utf-8">
<title>Vorlinex – Surplus Source Email</title>
<link rel="stylesheet" href="https://fonts.googleapis.com/css2?family=Montserrat:wght@300;400;500;600;700&display=swap">
<style>
:root{
  --bg:#bdbdbd;
  --white:#ffffff;
  --blue:#2a7bc0;
  --navy:#0e3e6c;
  --charcoal:#3a3a3a;
  --text:#555555;
  --muted:#8a8a8a;
  --panel:#f4f4f4;
  --line:#dcdcdc;
}
*{margin:0;padding:0;box-sizing:border-box}
html,body{width:1200px;height:3008px;overflow:hidden;background:var(--bg);font-family:'Montserrat',sans-serif}
.email{position:absolute;left:128px;top:4px;width:472px;height:1500px;background:var(--white);transform:scale(2);transform-origin:0 0;overflow:hidden;box-shadow:0 6px 20px rgba(0,0,0,.15)}
.abs{position:absolute}
.center{left:0;width:100%;text-align:center}
.browser-link{left:22px;top:12px;font-size:6.5px;color:var(--muted);text-decoration:underline}
.social{position:absolute;width:18px;height:18px;border:1px solid var(--blue);border-radius:50%}
.hero{left:0;top:34px;width:472px;height:240px;background:linear-gradient(160deg,#2e4766 0%,#1d3352 45%,#3a5478 100%)}
.hero-shape{left:0;top:0}
.brand{font-size:12px;font-weight:600;color:var(--navy);letter-spacing:1.5px}
.hero-title{top:134px;font-size:22.5px;font-weight:300;color:var(--white);line-height:26px;letter-spacing:.2px}
.intro{top:314px;font-size:11.2px;color:var(--text);line-height:19px;font-weight:400}
.intro a{color:var(--blue);font-weight:700;text-decoration:underline}
.tile{position:absolute;top:393px;width:131px;height:172px}
.tile-label{position:absolute;left:0;width:100%;top:114px;text-align:center;font-size:8.6px;font-weight:600;color:var(--white)}
.tile-icon{position:absolute;left:35px;top:36px}
.btn{position:absolute;height:28px;border:1px solid var(--navy);background:var(--white);display:flex;align-items:stretch}
.btn span{display:flex;align-items:center;padding:0 10px;font-size:7.8px;font-weight:600;color:var(--navy);border-right:1px solid var(--navy)}
.btn i{flex:1;display:flex;align-items:center;justify-content:center}
.know{left:0;top:676px;width:472px;height:329px;background:var(--panel)}
.know-title{top:34px;font-size:19px;font-weight:500;color:var(--navy);letter-spacing:.5px}
.know-rule{left:219px;top:60px;width:34px;height:1px;background:var(--navy)}
.stat-top{left:22px;top:91px;width:222px;height:67px;background:var(--blue)}
.stat-bottom{left:22px;top:158px;width:222px;height:86px;background:var(--charcoal)}
.stat-only{left:19px;top:38px;font-size:12px;color:var(--white)}
.stat-num{left:57px;top:4px;font-size:50px;font-weight:700;color:var(--white);letter-spacing:-2px}
.stat-text{left:19px;top:31px;font-size:11px;line-height:18px;color:#e2e2e2;font-weight:300}
.stat-text b{font-weight:700;color:var(--white)}
.stat-photo{left:246px;top:91px;width:204px;height:153px;background:linear-gradient(135deg,#c9c3bb 0%,#8c837a 40%,#6a5a4b 60%,#9fa8ad 100%)}
.band{left:0;top:1005px;width:472px;height:57px;background:var(--navy);color:var(--white);font-size:19px;font-weight:500;text-align:center;line-height:57px;letter-spacing:.3px}
.list{left:96px;top:1091px;width:280px}
.row{height:46px;border-top:1px solid var(--line);display:flex;align-items:center;position:relative}
.row:last-child{border-bottom:1px solid var(--line)}
.row-icon{width:67px;padding-left:12px}
.row-text{flex:1;font-size:7.6px;font-weight:500;color:var(--navy)}
.row-arrow{padding-right:12px}
.footer{left:0;top:1268px;width:472px;height:232px;background:var(--panel)}
.foot-mail{top:86px;font-size:11px;font-weight:700;color:var(--charcoal)}
.foot-addr{top:116px;font-size:9.5px;line-height:18px;color:var(--text)}
.foot-rule{left:58px;top:200px;width:356px;height:1px;background:var(--line)}
.foot-copy{top:210px;font-size:7.8px;color:var(--muted)}
</style>
</head>
<body>
<main class="email">
  <!-- header -->
  <a class="abs browser-link">View in browser?</a>
  <span class="social" style="left:407px;top:8px"></span>
  <span class="social" style="left:432px;top:8px"></span>

  <!-- hero -->
  <div class="abs hero" role="img" aria-label="Photograph of stacked steel pipes in a warehouse, blue tinted"></div>
  <svg class="abs hero-shape" width="472" height="290" viewBox="0 0 472 290">
    <polygon points="150,33 322,33 295,75 172,75" fill="#ffffff"/>
    <polygon points="0,237 236,272 472,237 472,290 0,290" fill="#ffffff"/>
    <polyline points="0,237 236,272 472,237" fill="none" stroke="#2a7bc0" stroke-width="3"/>
  </svg>
  <div class="abs center brand" style="top:22px">VORLINEX</div>
  <h1 class="abs center hero-title">THE ONLY TRUSTED<br>SURPLUS SOURCE FROM &amp; FOR<br>CONTRACTORS</h1>

  <p class="abs center intro">Browse thousands of certified inventory materials from trusted<br>sources and <a>save up to 70%</a> on your projects</p>

  <!-- service tiles -->
  <div class="tile" style="left:39px">
    <svg width="131" height="172"><polygon points="65.5,0 131,17 131,155 65.5,172 0,155 0,17" fill="#2a7bc0"/></svg>
    <svg class="tile-icon" width="60" height="50" viewBox="0 0 60 50" fill="none" stroke="#fff" stroke-width="2.2">
      <line x1="14" y1="9" x2="46" y2="9"/><line x1="10" y1="14" x2="50" y2="14"/>
      <rect x="3" y="19" width="54" height="25" rx="2"/>
      <circle cx="30" cy="31.5" r="8" fill="#fff"/>
      <text x="30" y="36" font-size="12" font-weight="700" fill="#2a7bc0" stroke="none" text-anchor="middle" font-family="Montserrat,sans-serif">$</text>
    </svg>
    <div class="tile-label">PURCHASE ORDER</div>
  </div>
  <div class="tile" style="left:171px">
    <svg width="131" height="172"><polygon points="65.5,0 131,17 131,155 65.5,172 0,155 0,17" fill="#3a3a3a"/></svg>
    <svg class="tile-icon" width="60" height="50" viewBox="0 0 60 50" fill="none" stroke="#fff" stroke-width="2">
      <path d="M24 34 C14 22 12 18 12 14 A12 12 0 0 1 36 14 C36 18 34 22 24 34Z"/>
      <circle cx="24" cy="14" r="5"/>
      <path d="M22 38 Q28 46 38 42 Q46 36 40 28 Q38 22 46 18" stroke-dasharray="2.5 2.5"/>
    </svg>
    <div class="tile-label">SHIPPING &amp; HANDLING</div>
  </div>
  <div class="tile" style="left:303px">
    <svg width="131" height="172"><polygon points="65.5,0 131,17 131,155 65.5,172 0,155 0,17" fill="#2a7bc0"/></svg>
    <svg class="tile-icon" width="60" height="50" viewBox="0 0 60 50" fill="none" stroke="#fff" stroke-width="2.2">
      <circle cx="30" cy="25" r="22"/>
      <polyline points="19,25 28,34 50,8"/>
    </svg>
    <div class="tile-label">MATERIAL WARRANTY</div>
  </div>

  <div class="btn" style="left:182px;top:610px;width:118px">
    <span>FIND OUT MORE</span>
    <i><svg width="10" height="10" viewBox="0 0 10 10" fill="none" stroke="#0e3e6c" stroke-width="1"><polyline points="2,1 6,5 2,9"/><polyline points="5,1 9,5 5,9"/></svg></i>
  </div>

  <!-- did you know -->
  <section class="abs know">
    <h2 class="abs center know-title">DID YOU KNOW?</h2>
    <div class="abs know-rule"></div>
    <div class="abs stat-top">
      <span class="abs stat-only">ONLY</span>
      <span class="abs stat-num">11%</span>
      <svg class="abs" style="left:172px;top:20px" width="30" height="30" viewBox="0 0 30 30" fill="none" stroke="#fff" stroke-width="2.4">
        <path d="M24 12 A10 10 0 0 0 6 10"/><polyline points="20,12 25,13 26,7"/>
        <path d="M6 18 A10 10 0 0 0 24 20" stroke-dasharray="3 2.5"/>
      </svg>
    </div>
    <div class="abs stat-bottom">
      <svg class="abs" style="left:83px;top:0" width="20" height="9"><polygon points="0,0 20,0 10,9" fill="#2a7bc0"/></svg>
      <p class="abs stat-text">Of spare materials circulate<br>back into the <b>market</b></p>
    </div>
    <div class="abs stat-photo" role="img" aria-label="Photograph of long steel pipes and beams stored in a yard"></div>
    <div class="btn" style="left:193px;top:267px;width:88px;height:27px">
      <span>EXPLORE</span>
      <i><svg width="10" height="10" viewBox="0 0 10 10" fill="none" stroke="#0e3e6c" stroke-width="1"><polyline points="2,1 6,5 2,9"/><polyline points="5,1 9,5 5,9"/></svg></i>
    </div>
  </section>

  <!-- solution -->
  <h2 class="abs band">VORLINEX SOLUTION</h2>
  <ul class="abs list">
    <li class="row">
      <span class="row-icon"><svg width="24" height="24" viewBox="0 0 24 24" fill="none" stroke="#2a7bc0" stroke-width="1.8"><circle cx="12" cy="12" r="10"/><path d="M15.5 8.5 Q12 6.5 9.5 8.5 Q8 11 12 12 Q16 13 14.5 15.5 Q12 17.5 8.5 15.5"/><line x1="12" y1="5" x2="12" y2="19"/><line x1="5" y1="5" x2="19" y2="19"/></svg></span>
      <span class="row-text">NO ADDITIONAL COSTS</span>
      <span class="row-arrow"><svg width="8" height="8" viewBox="0 0 10 10" fill="none" stroke="#2a7bc0"><polyline points="2,1 6,5 2,9"/><polyline points="5,1 9,5 5,9"/></svg></span>
    </li>
    <li class="row">
      <span class="row-icon"><svg width="24" height="24" viewBox="0 0 24 24" fill="none" stroke="#2a7bc0" stroke-width="1.8"><polyline points="3,9 3,3 9,3"/><line x1="3" y1="3" x2="9" y2="9"/><polyline points="15,3 21,3 21,9"/><line x1="21" y1="3" x2="15" y2="9"/><polyline points="3,15 3,21 9,21"/><line x1="3" y1="21" x2="9" y2="15"/><polyline points="21,15 21,21 15,21"/><line x1="21" y1="21" x2="15" y2="15"/></svg></span>
      <span class="row-text">VAST NETWORK REACH</span>
      <span class="row-arrow"><svg width="8" height="8" viewBox="0 0 10 10" fill="none" stroke="#2a7bc0"><polyline points="2,1 6,5 2,9"/><polyline points="5,1 9,5 5,9"/></svg></span>
    </li>
    <li class="row">
      <span class="row-icon"><svg width="24" height="24" viewBox="0 0 24 24" fill="none" stroke="#2a7bc0" stroke-width="1.8"><path d="M2 6 H7 L15 18 H21"/><path d="M2 18 H7 L9.5 14"/><path d="M12.5 10 L15 6 H21"/><polyline points="18,3 21,6 18,9"/><polyline points="18,15 21,18 18,21"/></svg></span>
      <span class="row-text">SIMPLE INTEGRATED SOLUTIONS</span>
      <span class="row-arrow"><svg width="8" height="8" viewBox="0 0 10 10" fill="none" stroke="#2a7bc0"><polyline points="2,1 6,5 2,9"/><polyline points="5,1 9,5 5,9"/></svg></span>
    </li>
  </ul>

  <!-- footer -->
  <footer class="abs footer">
    <svg class="abs" style="left:0;top:0" width="472" height="60"><polygon points="143,0 329,0 283,57 188,57" fill="#ffffff"/></svg>
    <div class="abs center brand" style="top:18px;font-size:11px">VORLINEX</div>
    <p class="abs center foot-mail">info@vorlinex.com</p>
    <p class="abs center foot-addr">800-VORLINEX License no. 058213<br>Marina Row, Dubai, UAE</p>
    <span class="social" style="left:214px;top:158px"></span>
    <span class="social" style="left:240px;top:158px"></span>
    <div class="abs foot-rule"></div>
    <p class="abs center foot-copy">Copyright © 2019 Vorlinex. All Rights Reserved</p>
  </footer>
</main>
</body>
</html>
```